Holvik Cabinets Quality Custom Built Kitchens, Vanity Units, Robes ect

Hi,
Was after a new design for our business cards,
we are a cabinet making business and pride ourselves in quality custom built Kitchens, Vanity units, robes ect.
we have been around for over 20 years and we are trying to modernize our card logo.
Looking for something eye catching, bold and exciting
family ran and operated business, we work with builders and also have a large private clientel.

Thanks

Industry/Entity Type

Business

Contact Information for Business Card

Holvik Cabinets

Font styles to use
Serif
Script

Requirements
Must have
• Corinne 0461735928 hvcabinets@mailvane.com
• Po Box 2786
• 5B Wattlebark Court Kelbridge Vic 3871
• Phone (03)59286417 Fax (03) 59286942
Nice to have
• Quality Custom Built Kitchens & Vanity Units

```html
<!DOCTYPE html>
<html lang="en">
<head>
<meta charset="utf-8">
<title>Holvik Cabinets – Business Card</title>
<link rel="stylesheet" href="https://fonts.googleapis.com/css2?family=Fira+Sans:wght@300;400;600&display=swap">
<style>
  :root {
    --page: #ffffff;
    --card: #1f1f20;
    --texture-light: #2a2a2b;
    --texture-dark: #1c1c1d;
    --gold: #c3922e;
    --text: #f2f2f2;
    --icon: #9a9a9a;
  }
  * { margin: 0; padding: 0; box-sizing: border-box; }
  html, body {
    width: 1200px;
    height: 749px;
    overflow: hidden;
    background: var(--page);
  }
  .card {
    position: relative;
    width: 1200px;
    height: 749px;
    font-family: "Fira Sans", Arial, sans-serif;
  }
  .card-shape {
    position: absolute;
    inset: 0;
  }
  .brand-name {
    position: absolute;
    left: 116px;
    top: 214px;
    font-weight: 600;
    font-size: 86px;
    letter-spacing: 1px;
    color: var(--gold);
    line-height: 1;
  }
  .contact-person {
    position: absolute;
    left: 114px;
    top: 428px;
    color: var(--text);
    line-height: 1;
  }
  .contact-name {
    font-weight: 300;
    font-size: 38px;
    color: var(--gold);
    text-transform: uppercase;
    margin-right: 14px;
  }
  .contact-mobile {
    font-size: 29px;
    font-weight: 400;
  }
  .contact-email {
    position: absolute;
    left: 114px;
    top: 476px;
    font-size: 29px;
    color: var(--text);
  }
  .office-details {
    position: absolute;
    left: 494px;
    top: 505px;
    font-size: 29px;
    color: var(--text);
    line-height: 48px;
  }
  .office-line {
    display: flex;
    align-items: center;
  }
  .office-line .icon {
    width: 30px;
    height: 30px;
    margin-right: 14px;
    fill: var(--icon);
    flex: none;
  }
  .office-line .indent { margin-left: 44px; }
  .fax { display: inline-flex; align-items: center; margin-left: 36px; }
  .fax .icon { margin-right: 10px; }
</style>
</head>
<body>
  <div class="card">
    <svg class="card-shape" width="1200" height="749" viewBox="0 0 1200 749" aria-hidden="true">
      <defs>
        <linearGradient id="texture-fill" x1="0" y1="0" x2="0" y2="1">
          <stop offset="0" stop-color="var(--texture-light)"/>
          <stop offset="1" stop-color="var(--texture-dark)"/>
        </linearGradient>
      </defs>
      <polygon points="32,46 1174,183 1174,718 32,718" fill="var(--card)"/>
    </svg>
    <svg class="card-shape" width="1200" height="749" viewBox="0 0 1200 749" role="img" aria-label="Subtle wavy line texture across the lower card band">
      <rect x="32" y="385" width="1142" height="333" fill="url(#texture-fill)"/>
    </svg>

    <h1 class="brand-name">HOLVIK CABINETS</h1>

    <p class="contact-person">
      <span class="contact-name">Corinne</span><span class="contact-mobile">0461735928</span>
    </p>
    <p class="contact-email">hvcabinets@mailvane.com</p>

    <div class="office-details">
      <p class="office-line">
        <svg class="icon" viewBox="0 0 24 24" aria-hidden="true"><path d="M12 2a7 7 0 0 0-7 7c0 5 7 13 7 13s7-8 7-13a7 7 0 0 0-7-7zm0 9.5A2.5 2.5 0 1 1 12 6.5a2.5 2.5 0 0 1 0 5z"/></svg>
        5B Wattlebark Court Kelbridge Vic 3871
      </p>
      <p class="office-line"><span class="indent">Po Box 2786</span></p>
      <p class="office-line">
        <svg class="icon" viewBox="0 0 24 24" aria-hidden="true"><path d="M3 8c0-2 4-4 9-4s9 2 9 4v2h-5V8c-1-.6-2.4-1-4-1s-3 .4-4 1v2H3zM6 12h12l2 7H4z"/></svg>
        Phone (03)59286417
        <span class="fax">
          <svg class="icon" viewBox="0 0 24 24" aria-hidden="true"><path d="M7 3h8l2 2v4H7zM4 10h16v8h-3v3H7v-3H4zm5 5v4h6v-4z"/></svg>
          (03) 59286942
        </span>
      </p>
    </div>
  </div>
</body>
</html>
```